We currently have a good logo and we want business cards that can display our logo but also represent our industry - telecom construction - We are a construction company specializing in telecom construction such as installation of fiber optic cable throughout cities and across the country. Nationwide services
We are large enough to handle most any project yet small enough to be a flexible partner and resource.

Target Market(s)

U.S. based telecom carriers and providers

Industry/Entity Type

Construction

Contact Information for Business Card

Business cards should include our logo, phone number and website address. Also, including some information as to our core services would be good.

Colors

Designer to choose colors to be used in the design.

Requirements
Must have
• Colors based on logo
• Must use our logo
• Logo, name, email, website address, phone number
• Tovasco Conduit
• Brent Halvik
• Director of Business Development
• (555) 271-0386
• www.TVSQ-example.com
Nice to have
• Construction services including:
• Small Cell Construction
• Boring/Drilling
• Plowing / Trenching
• Conduit installation
• Fiber pulling
• splicing
• building entries
• Aerial construction
• Aerial Make Ready
• Make Ready Engineering
Should not have
• We are open to ideas

```html
<!DOCTYPE html>
<html lang="en">
<head>
<meta charset="utf-8">
<title>Tovasco Conduit – Business Cards</title>
<link href="https://fonts.googleapis.com/css2?family=Arimo:wght@400;700&display=swap" rel="stylesheet">
<style>
  :root {
    --bg: #e4e4e4;
    --blue-deep: #0b5cb8;
    --blue-mid: #1a7fd6;
    --blue-light: #2aa3ec;
    --brand-blue: #1166c4;
    --accent-blue: #1e8fe0;
    --ink: #333333;
    --ink-soft: #555555;
    --white: #ffffff;
    --divider: #c9c9c9;
  }
  * { box-sizing: border-box; margin: 0; padding: 0; }
  html, body { width: 1200px; height: 900px; overflow: hidden; }
  body {
    background: var(--bg);
    font-family: "Arimo", Arial, sans-serif;
    position: relative;
  }
  .card {
    position: absolute;
    width: 525px;
    height: 300px;
    border-radius: 22px;
    box-shadow: 0 10px 24px rgba(0,0,0,0.22);
    overflow: hidden;
  }
  .brand-name {
    position: absolute;
    font-weight: 700;
    line-height: 1.05;
    letter-spacing: 0.5px;
  }
  .brand-name span { display: block; }

  /* Front: services */
  .card-front {
    left: 55px; top: 130px;
    background: linear-gradient(160deg, var(--blue-deep) 0%, var(--blue-mid) 55%, var(--blue-light) 100%);
    color: var(--white);
  }
  .card-front .brand-name {
    left: 48px; top: 112px;
    font-size: 38px;
    color: var(--white);
  }
  .services {
    position: absolute;
    left: 290px; top: 46px;
    list-style: none;
    font-size: 15px;
    line-height: 20.5px;
  }
  .services li { position: relative; padding-left: 16px; }
  .services li::before {
    content: "";
    position: absolute; left: 0; top: 7px;
    width: 6px; height: 6px; border-radius: 50%;
    background: var(--white);
  }

  /* Back: contact */
  .card-back {
    left: 610px; top: 470px;
    background: var(--white);
    color: var(--ink);
  }
  .card-back .brand-name {
    left: 52px; top: 110px;
    font-size: 38px;
    color: var(--brand-blue);
  }
  .divider {
    position: absolute;
    left: 250px; top: 62px;
    width: 2px; height: 176px;
    background: var(--divider);
  }
  .contact { position: absolute; left: 272px; top: 66px; }
  .person-name {
    font-size: 20px; font-weight: 700;
    color: var(--accent-blue);
    letter-spacing: 0.5px;
  }
  .person-title { font-size: 14px; color: var(--ink-soft); margin-top: 2px; }
  .contact-list { list-style: none; margin-top: 18px; }
  .contact-list li {
    display: flex; align-items: center; gap: 9px;
    font-size: 17px; color: var(--ink);
    height: 28px;
  }
  .icon {
    width: 20px; height: 20px; border-radius: 4px;
    background: var(--accent-blue);
    display: flex; align-items: center; justify-content: center;
    flex-shrink: 0;
  }
</style>
</head>
<body>
  <section class="card card-front" aria-label="Business card front">
    <div class="brand-name"><span>Tovasco</span><span>Conduit</span></div>
    <ul class="services">
      <li>Small Cell Construction</li>
      <li>Boring/Drilling</li>
      <li>Plowing / Trenching</li>
      <li>Conduit installation</li>
      <li>Fiber pulling</li>
      <li>Splicing</li>
      <li>Building entries</li>
      <li>Aerial construction</li>
      <li>Aerial Make Ready</li>
      <li>Make Ready Engineering</li>
    </ul>
  </section>

  <section class="card card-back" aria-label="Business card back">
    <div class="brand-name"><span>Tovasco</span><span>Conduit</span></div>
    <div class="divider"></div>
    <div class="contact">
      <div class="person-name">BRENT HALVIK</div>
      <div class="person-title">Director of Business Development</div>
      <ul class="contact-list">
        <li>
          <span class="icon">
            <svg width="13" height="13" viewBox="0 0 24 24"><path fill="#fff" d="M6.6 10.8a15.1 15.1 0 0 0 6.6 6.6l2.2-2.2c.3-.3.7-.4 1-.2 1.1.4 2.3.6 3.6.6.6 0 1 .4 1 1V20c0 .6-.4 1-1 1C10.6 21 3 13.4 3 4c0-.6.4-1 1-1h3.5c.6 0 1 .4 1 1 0 1.3.2 2.5.6 3.6.1.3 0 .7-.2 1z"/></svg>
          </span>
          (555) 271-0386
        </li>
        <li>
          <span class="icon">
            <svg width="13" height="13" viewBox="0 0 24 24"><path fill="#fff" d="M3 5h18v14H3z"/><path fill="none" stroke="#1e8fe0" stroke-width="2" d="M3 6l9 7 9-7"/></svg>
          </span>
          info@tvsq-example.com
        </li>
        <li>
          <span class="icon">
            <svg width="13" height="13" viewBox="0 0 24 24"><circle cx="12" cy="12" r="9" fill="none" stroke="#fff" stroke-width="2"/><path d="M3 12h18M12 3c3 3 3 15 0 18M12 3c-3 3-3 15 0 18" fill="none" stroke="#fff" stroke-width="1.6"/></svg>
          </span>
          www.TVSQ-example.com
        </li>
      </ul>
    </div>
  </section>
</body>
</html>
```